Bright Cabin Works Needs a Flyer

We need a new flyer for our Garden Nook Tavern. (Photos attached)

We would like to place the bar close to a nice swimming pool that would be in someone's back yard in Florida.

1. Add solar panels. Solar is installed on rails so they sit 2"-3" off the roof.
3. Add a still frame of the Coral Herons football game on the TV.
4. The over all color scheme should be colors that compliment pools and
back patios like blues. Not green or orange. Don't try to match our
logo.

4. Make the bar and pool the central main photo.

Here is some copy for the flyer:

"Your pool is lonely! Introducing our stunning solar powered Garden Nook Tavern!"

"Expand the value of your outdoor living with the ultimate Entertianment venue"

Bullets:

- Dimensions: 5' deep x 10' wide x 9-6'. Enough seating for 6-8 people.
- Comes FULLY assembled. You can't reach this level of quality in a kit.
- 1 coat of primer, two coats of Havelock Prime Glossmark paint for
extreme weather.
- 150 MPH rated Brantley Hale shingles
- TV mount included in the base configuration.
- Options include, pendant lights, hard surface floor, flip up shelf on short
side, bar stools, cabinets, portable sinks, keg tap installs. wine shelves ,
copper wine glasses, liquor shelves and more!

"Solar versions have enough solar and batteries to power your TV, lights, mini fridge, cell phones and more. The advanced Lithium Phosphate Batteries are very safe and can power everything for up to 48 hours without sun."

"Visit our website and mention "Coastal Glow" in the comments section and receive a free Kodo cooler when you order your new Garden Nook Tavern!"

"Visit www.BrightCabinWorks.example/GardenNookTavern to learn more!"

```html
<!DOCTYPE html>
<html lang="en">
<head>
<meta charset="utf-8">
<title>Garden Nook Tavern Flyer</title>
<link rel="stylesheet" href="https://fonts.googleapis.com/css2?family=Arimo:wght@400;700&family=Bowlby+One+SC&display=swap">
<style>
  :root {
    --page-bg: #ece4df;
    --charcoal: #2a2a2a;
    --lime: #4cc13a;
    --band: #6ec645;
    --teal-head: #14a696;
    --teal-panel: #0f6e71;
    --deep-panel: #05252a;
    --white: #ffffff;
    --photo-sky: #9fb3a8;
    --photo-garden: #3f6a35;
    --photo-pool: #3aa7d6;
    --photo-deck: #c9c6c0;
  }
  * { box-sizing: border-box; margin: 0; padding: 0; }
  html, body { width: 1200px; height: 900px; overflow: hidden; }
  body { background: var(--page-bg); position: relative; font-family: "Arimo", Arial, sans-serif; }

  .flyer {
    position: absolute; left: 270px; top: 23px;
    width: 660px; height: 854px; overflow: hidden;
    background: linear-gradient(180deg, var(--teal-panel) 50%, #0a4a4f 78%, var(--deep-panel) 100%);
  }
  .hero-photo {
    position: absolute; left: 0; top: 0; width: 660px; height: 440px;
    background:
      linear-gradient(180deg, var(--photo-sky) 0%, var(--photo-garden) 28%, var(--photo-garden) 40%, var(--photo-pool) 52%, var(--photo-pool) 72%, var(--photo-deck) 86%);
  }
  .torn-edge { position: absolute; left: 0; top: 418px; width: 660px; height: 40px; }

  .brand-tile {
    position: absolute; left: 467px; top: 0; width: 168px; height: 150px;
    background: var(--white); border-radius: 0 0 14px 14px;
    display: flex; align-items: center; justify-content: center; gap: 6px;
  }
  .brand-tile .brand-dot { width: 12px; height: 12px; border-radius: 50%; background: var(--teal-panel); flex: none; }
  .brand-tile .brand-name {
    font-family: "Bowlby One SC", Impact, sans-serif; font-size: 15px; line-height: 1.1;
    color: var(--teal-panel); text-align: center; width: 120px;
  }

  .headline {
    position: absolute; left: 240px; width: 420px; text-align: center;
    font-family: "Bowlby One SC", Impact, sans-serif; line-height: 0.98;
    paint-order: stroke fill;
  }
  .headline-lonely {
    top: 190px; font-size: 44px; color: var(--charcoal);
    -webkit-text-stroke: 4px var(--lime);
  }
  .intro-band {
    position: absolute; left: 307px; top: 293px; width: 288px; height: 26px;
    background: var(--band); color: var(--charcoal);
    font-family: "Bowlby One SC", Impact, sans-serif; font-size: 15px;
    display: flex; align-items: center; justify-content: center;
  }
  .headline-product {
    top: 330px; font-size: 29px; color: var(--teal-head);
    -webkit-text-stroke: 4px var(--charcoal); letter-spacing: -0.5px;
  }

  .value-heading {
    position: absolute; left: 120px; top: 468px; width: 450px; text-align: center;
    font-family: "Bowlby One SC", Impact, sans-serif; font-size: 16px; line-height: 1.1;
    color: var(--lime);
  }

  .feature-list { position: absolute; left: 52px; top: 540px; width: 330px; list-style: none; }
  .feature-list li {
    position: relative; padding-left: 32px; margin-bottom: 12px;
    color: var(--white); font-size: 10.5px; line-height: 1.25;
  }
  .feature-list .tick { position: absolute; left: 0; top: -4px; width: 22px; height: 22px; }

  .solar-callout { position: absolute; left: 392px; top: 537px; width: 254px; height: 180px; }
  .solar-callout svg { position: absolute; inset: 0; }
  .solar-callout p {
    position: absolute; left: 28px; top: 22px; width: 198px; text-align: center;
    color: var(--white); font-weight: 700; font-size: 11.5px; line-height: 1.33;
  }

  .offer-note {
    position: absolute; left: 50px; top: 778px; width: 232px; text-align: center;
    color: var(--white); font-size: 12px; line-height: 1.3;
  }
  .site-cta {
    position: absolute; left: 318px; top: 790px; width: 340px; text-align: center;
    color: var(--white); font-weight: 700; font-size: 11px; line-height: 1.4;
  }
</style>
</head>
<body>
  <article class="flyer">
    <div class="hero-photo" role="img" aria-label="Photo of a backyard swimming pool in Florida with a dark solar-roofed Garden Nook Tavern bar, guests at the counter, a TV showing a Coral Herons football game, a black dog and pumpkins on the deck"></div>

    <svg class="torn-edge" viewBox="0 0 660 40" preserveAspectRatio="none" aria-hidden="true">
      <path d="M0 10 L20 6 L38 12 L60 5 L82 11 L104 4 L130 10 L150 7 L176 13 L200 6 L226 11 L250 5 L276 12 L300 8 L326 13 L350 6 L378 11 L402 5 L428 12 L452 7 L478 13 L502 6 L528 11 L552 5 L578 12 L604 7 L630 11 L660 4 L660 20 L636 24 L610 19 L584 25 L558 20 L530 26 L504 21 L478 26 L452 20 L426 25 L400 19 L374 26 L348 21 L322 25 L296 20 L270 26 L244 21 L218 25 L192 19 L166 26 L140 21 L114 25 L88 20 L62 26 L36 21 L0 25 Z" fill="#ffffff"/>
    </svg>

    <div class="brand-tile">
      <span class="brand-dot"></span>
      <span class="brand-name">Bright Cabin Works</span>
    </div>

    <h1 class="headline headline-lonely">Your pool is<br>lonely!</h1>
    <div class="intro-band">Introducing our stunning</div>
    <h2 class="headline headline-product">Solar powered<br>Garden Nook Tavern!</h2>

    <h3 class="value-heading">Expand the value of your<br>outdoor living with the ultimate<br>entertianment venue</h3>

    <ul class="feature-list">
      <li><svg class="tick" viewBox="0 0 22 22"><rect x="2" y="5" width="14" height="14" fill="none" stroke="#4cc13a" stroke-width="2.2"/><path d="M5 11 L9 16 L20 2" fill="none" stroke="#4cc13a" stroke-width="2.6" stroke-linecap="round" stroke-linejoin="round"/></svg>Dimensions: 5' deep x 10' wide x 9-6'.<br>Enough seating for 6-8 people.</li>
      <li><svg class="tick" viewBox="0 0 22 22"><rect x="2" y="5" width="14" height="14" fill="none" stroke="#4cc13a" stroke-width="2.2"/><path d="M5 11 L9 16 L20 2" fill="none" stroke="#4cc13a" stroke-width="2.6" stroke-linecap="round" stroke-linejoin="round"/></svg>Comes FULLY assembled. You can't reach this level of quality in a kit.</li>
      <li><svg class="tick" viewBox="0 0 22 22"><rect x="2" y="5" width="14" height="14" fill="none" stroke="#4cc13a" stroke-width="2.2"/><path d="M5 11 L9 16 L20 2" fill="none" stroke="#4cc13a" stroke-width="2.6" stroke-linecap="round" stroke-linejoin="round"/></svg>1 coat of primer, two coats of Havelock Prime Glossmark paint for extreme weather.</li>
      <li><svg class="tick" viewBox="0 0 22 22"><rect x="2" y="5" width="14" height="14" fill="none" stroke="#4cc13a" stroke-width="2.2"/><path d="M5 11 L9 16 L20 2" fill="none" stroke="#4cc13a" stroke-width="2.6" stroke-linecap="round" stroke-linejoin="round"/></svg>150 MPH rated Brantley Hale shingles</li>
      <li><svg class="tick" viewBox="0 0 22 22"><rect x="2" y="5" width="14" height="14" fill="none" stroke="#4cc13a" stroke-width="2.2"/><path d="M5 11 L9 16 L20 2" fill="none" stroke="#4cc13a" stroke-width="2.6" stroke-linecap="round" stroke-linejoin="round"/></svg>TV mount included in the base configuration.</li>
      <li><svg class="tick" viewBox="0 0 22 22"><rect x="2" y="5" width="14" height="14" fill="none" stroke="#4cc13a" stroke-width="2.2"/><path d="M5 11 L9 16 L20 2" fill="none" stroke="#4cc13a" stroke-width="2.6" stroke-linecap="round" stroke-linejoin="round"/></svg>Options include, pendant lights, hard surface floor, flip up shelf on short side, bar stools, cabinets, portable sinks, keg tap installs. wine shelves , copper wine glasses, liquor shelves and more!</li>
    </ul>

    <div class="solar-callout">
      <svg viewBox="0 0 254 180" aria-hidden="true">
        <path d="M40 12 C110 -2 210 4 240 30 C258 60 252 130 226 158 C190 182 70 182 30 162 C2 140 0 70 16 36 C26 20 60 10 110 8" fill="none" stroke="#ffffff" stroke-width="3" stroke-linecap="round"/>
        <path d="M52 18 C120 6 214 12 236 40 C248 80 242 132 220 152 C180 174 80 176 38 154" fill="none" stroke="#ffffff" stroke-width="1.4" stroke-linecap="round"/>
      </svg>
      <p>Solar versions have enough solar and batteries to power your TV, lights, mini fridge, cell phones and more. The advanced Lithium Phosphate Batteries are very safe and can power everything for up to 48 hours without sun.</p>
    </div>

    <p class="offer-note">Visit our website and mention "Coastal Glow" in the comments section and receive a free Kodo cooler when you order your new Garden Nook Tavern!</p>
    <p class="site-cta">Visit<br>www.BrightCabinWorks.example/GardenNookTavern<br>to learn more!</p>
  </article>
</body>
</html>
```